The Corvane Agency

We are a pr, social media and strategy agency specializing in the pet industry. We would like a new dynamic design of our existing website. We think it is currently outdated and looks too corporate. We would like it to look more consumer oriented as we primarily market pet products. We would like warm imagery involving pets and while pets are fun, this is still a business website and needs to maintain a professional look. We are hired by business owners and executives.
I would like some of our work featured on the home page.
Our primary service tabs are:
Public Relations
Social Media
Product Consulting
Most of the content will remain the same but we are open to suggestions!
Our current website can be found at www.corvanepetpr.example.
We are open to other colors than in our logo and on our current page.
This is a design only project and will not require programming. The selected designer will need to provide at least one interior page in addition to the home page.

Industry/Entity Type

Pet

Requirements
Should not have
• Cartoon type figures. Pet puns.

```html
<!DOCTYPE html>
<html lang="en">
<head>
<meta charset="utf-8">
<title>The Corvane Agency</title>
<link href="https://fonts.googleapis.com/css2?family=Alegreya:ital@1&family=Open+Sans:wght@400;600&family=Montserrat:wght@700&family=Cantarell&display=swap" rel="stylesheet">
<style>
:root{
  --orange:#b8661a;
  --orange-light:#cf7d2c;
  --orange-text:#c87b2e;
  --wood-dark:#1f140f;
  --wood:#2b1d16;
  --footer:#150e0a;
  --white:#ffffff;
  --text:#e6ddd5;
  --muted:#b9aca2;
  --brand:#d4202a;
}
*{margin:0;padding:0;box-sizing:border-box}
html,body{width:921px;height:1200px;overflow:hidden}
body{
  font-family:"Open Sans",sans-serif;color:var(--text);
  background:repeating-linear-gradient(90deg,var(--wood) 0 7px,#261912 7px 11px,#2e2018 11px 16px);
  position:relative;
}
.site-header{height:58px;background:var(--white);position:relative}
.brand{position:absolute;left:115px;top:15px;color:var(--brand);font-family:"Open Sans",sans-serif;font-size:21px;font-weight:400;display:flex;align-items:center;gap:5px}
.brand-dot{width:5px;height:5px;background:var(--brand);border-radius:50%}
.main-nav{position:absolute;right:80px;top:0;display:flex;height:58px}
.main-nav a{display:flex;align-items:center;padding:0 8px;font-size:8px;color:#333;text-decoration:none;letter-spacing:.2px}
.main-nav a.active{background:var(--orange);color:var(--white);height:58px}
.hero{position:absolute;left:115px;top:76px;width:691px;height:291px;border-radius:3px;overflow:hidden;background:linear-gradient(160deg,#f4f4f4,#d9d9d9)}
.hero-photo{position:absolute;right:0;top:0;width:390px;height:291px;background:linear-gradient(120deg,#c9905a,#e8c39a 55%,#f3e2cc)}
.hero-swoosh{position:absolute;left:0;top:0}
.hero-title{position:absolute;left:41px;top:54px;font-family:"Montserrat",sans-serif;color:var(--white);line-height:1}
.hero-title .l1{font-size:37px;display:block;letter-spacing:-.5px}
.hero-title .l2{font-size:27px;display:block;margin-top:2px}
.learn-more{position:absolute;left:150px;top:129px;width:104px;height:104px;border-radius:50%;background:#241813;border:3px solid #8c4e14;display:flex;align-items:center;justify-content:center;text-align:center;font-family:"Montserrat",sans-serif;color:var(--orange-light);font-size:19px;line-height:1}
.slider-dots{position:absolute;left:74px;top:178px;width:90px;height:36px;background:#241813;border-radius:18px;display:flex;align-items:center;gap:5px;padding-left:11px}
.slider-dots i{width:11px;height:11px;border-radius:50%;background:var(--orange)}
.slider-dots i.on{background:var(--white)}
.social-rail{position:absolute;right:0;top:145px;width:34px;height:131px;background:var(--orange);border-radius:4px 0 0 4px;display:flex;flex-direction:column;align-items:center;justify-content:space-around;padding:8px 0}
.social-rail i{width:8px;height:8px;background:var(--white);border-radius:2px}
.divider{position:absolute;left:145px;width:630px;height:1px;background:#3f2d22}
.pet-mark{position:absolute;left:435px;top:400px;width:47px;height:24px;background:linear-gradient(90deg,#8c4e14,#b8661a);border-radius:6px}
.services{position:absolute;left:145px;top:449px;display:flex;gap:8px}
.service-btn{height:37px;background:linear-gradient(#d07d2b,#b1621a);border:1px solid #d99448;border-radius:2px;display:flex;align-items:center;color:var(--white);font-size:14px;padding-left:14px;gap:20px}
.service-btn .icon{width:20px;height:16px;border:2px solid var(--white);border-radius:50%}
.welcome{position:absolute;left:205px;top:540px;width:510px;text-align:center}
.welcome h1{font-family:"Alegreya",serif;font-style:italic;font-weight:400;font-size:23px;color:var(--white);margin-bottom:18px}
.welcome h1 span{color:var(--orange-text)}
.welcome p{font-size:7.4px;line-height:13.3px;margin-bottom:13px}
.welcome .lead{font-family:"Cantarell",sans-serif;font-size:12px;color:var(--white);margin-top:-2px}
.work-strip{position:absolute;left:144px;top:810px;display:flex;gap:3px}
.work-strip div{width:124px;height:82px;border-radius:2px}
.columns{position:absolute;left:143px;top:935px;width:634px;display:flex;justify-content:space-between}
.col{width:194px;text-align:center}
.col h2{font-family:"Alegreya",serif;font-style:italic;font-weight:400;font-size:16px;color:var(--orange-text);margin-bottom:14px}
.col p{font-size:7.6px;line-height:13.3px;text-align:justify;text-align-last:center}
.read-more{display:block;margin-top:12px;font-size:8px;color:var(--orange-text);text-decoration:none}
.quote-name{margin-top:12px;font-size:10px;color:var(--white)}
.quote-role{font-size:8px}
.posts{list-style:none}
.posts li{font-size:7.6px;height:25px;line-height:25px}
.posts li.hover{background:#1c120d;border-radius:3px}
.site-footer{position:absolute;left:0;top:1150px;width:921px;height:50px;background:var(--footer);font-size:7.4px;color:var(--muted)}
.foot-nav{position:absolute;left:144px;top:20px;display:flex;gap:9px}
.foot-nav a{color:var(--muted);text-decoration:none}
.foot-nav a:first-child{color:var(--white)}
.copyright{position:absolute;left:502px;top:20px;font-family:"Alegreya",serif;font-style:normal;color:var(--text)}
.copyright span{color:var(--orange-text)}
.to-top{position:absolute;left:818px;top:16px;width:19px;height:19px;background:var(--orange);border-radius:2px}
.to-top svg{display:block}
</style>
</head>
<body>
<header class="site-header">
  <div class="brand"><span class="brand-dot"></span>The Corvane Agency</div>
  <nav class="main-nav">
    <a class="active" href="#">HOME</a><a href="#">PR</a><a href="#">SOCIAL MEDIA</a><a href="#">PET EXPERTS</a><a href="#">BUSINESS DEVELOPMENT</a><a href="#">CASE STUDIES</a><a href="#">OUR TEAM</a>
  </nav>
</header>

<section class="hero">
  <div class="hero-photo" role="img" aria-label="Photo of a woman holding a rabbit close to her face"></div>
  <svg class="hero-swoosh" width="691" height="291" viewBox="0 0 691 291">
    <path d="M0 0H691V0Q560 20 450 70Q300 150 180 170Q80 185 0 150Z" fill="#b8661a"/>
  </svg>
  <div class="hero-title"><span class="l1">REDEFINING</span><span class="l2">PET SERVICE</span></div>
  <div class="slider-dots"><i></i><i class="on"></i><i></i><i></i></div>
  <div class="learn-more">LEARN<br>MORE</div>
</section>

<aside class="social-rail"><i></i><i></i><i></i><i></i><i></i></aside>

<div class="divider" style="top:412px"></div>
<div class="pet-mark" role="img" aria-label="Small dog and cat silhouette"></div>

<nav class="services">
  <a class="service-btn" style="width:215px"><span class="icon"></span>PUBLIC RELATIONS</a>
  <a class="service-btn" style="width:179px"><span class="icon"></span>SOCIAL MEDIA</a>
  <a class="service-btn" style="width:242px"><span class="icon"></span>PRODUCT CONSULTING</a>
</nav>

<div class="divider" style="top:520px"></div>

<section class="welcome">
  <h1>Welcome to <span>Corvane</span></h1>
  <p>The word "Corvane" has great meaning to us. It's the force that makes things happen, the motivation that turns nothing into something. For us, that stimulus is generated by a corporate culture that allows work to flow freely, projects to progress quickly, and ideas to flourish naturally. There really was no other name in the world that was a better fit. We specialize in the pet industry through a team effort built on passionate individuals who understand the unique aspects of the multi-billion dollar pet industry. It's not a culture you'll find just anywhere. Achieving that perfect balance of public relations leadership skills, in-the-trenches attitude, team chemistry, and unified vision is something The Corvane Agency has worked diligently to hone.</p>
  <p>All that hard work translates into success for our clients. We tap the best ways to connect you with your audience, using modern marketing platforms and a full arsenal of social media outlets to speak to your audience on a level that is more specific, more engaging, and most of all, more personable. As the world continues to evolve with new tools and technologies, our team is going beyond just keeping up with the latest methods of effective communication.</p>
  <p class="lead">We're leading the way.</p>
</section>

<div class="divider" style="top:797px"></div>

<section class="work-strip">
  <div role="img" aria-label="White parrots on a branch" style="background:linear-gradient(#5d6f86,#c9ccd0)"></div>
  <div role="img" aria-label="Boy with a shaggy dog" style="background:linear-gradient(#2f5fb0,#c6a06a)"></div>
  <div role="img" aria-label="Yellow tropical fish" style="background:linear-gradient(#3a3f46,#d9b21c)"></div>
  <div role="img" aria-label="Two small terriers on red" style="background:linear-gradient(#b51d2a,#8e1a22)"></div>
  <div role="img" aria-label="Child hugging a puppy on yellow" style="background:linear-gradient(#e8c21a,#c08a3e)"></div>
</section>

<div class="divider" style="top:905px"></div>

<section class="columns">
  <div class="col">
    <h2>Our Team</h2>
    <p>The driving force behind our success is the team that makes it happen. Individual skills and experience meet a collective desire to excel in every facet of our work and shape our daily approach to elevate the pet industry through our clients. Each member of our pack provides the strength and stability to run smoothly, yet it's our unified vision to always stay hungry, curious and happy ...</p>
    <a class="read-more" href="#">Read More</a>
  </div>
  <div class="col">
    <h2>Testimonials</h2>
    <p>The Corvane Agency has been a huge asset to us from the beginning. In the initial launch of Pawvista, they opened tremendous channels to numerous media outlets. They continued to provide industry exposure with skilled and experience social media guidance. Traditional media would have been costly, Corvane has been a great ROI for us.</p>
    <div class="quote-name">- Dana Whitlock</div>
    <div class="quote-role">Managing Director, Pawvista, Inc.</div>
  </div>
  <div class="col">
    <h2>Recent Blog Posts</h2>
    <ul class="posts">
      <li>Trailhound Featured on Daybreak Live</li>
      <li>The Power of Stress</li>
      <li class="hover">The Evolution of the Ideas: Brainstorming</li>
      <li>Can Giving Go Viral?</li>
      <li>Relationship Building</li>
    </ul>
  </div>
</section>

<footer class="site-footer">
  <nav class="foot-nav"><a href="#">Contact</a><a href="#">Careers</a><a href="#">Love list</a><a href="#">Blog</a><a href="#">Site Map</a></nav>
  <div class="copyright">©2014 The Corvane Agency | 48 Alder Ridge Rd. NV 89000 | <span>555.014.2290</span></div>
  <a class="to-top" href="#"><svg width="19" height="19" viewBox="0 0 19 19"><path d="M6 11L9.5 7.5L13 11" stroke="#fff" stroke-width="2" fill="none"/></svg></a>
</footer>
</body>
</html>
```